Animal Eye Clinic needs a Business card

We are a new veterinary ophthalmology practice (Tessaly Animal Eye Care) and we need a business card designed. We only see animal eyes - we are not a regular veterinary clinic. We already have a logo. We are looking for a professional, good looking business card to hand out to our clients. We are looking for something simple but professional and contemporary. Our logo is likely the only picture/graphic that needs to be on the card.
Updates

Contact Information for Business Card

Marisol Dunkley, BSc, DVM, MSc, DipACVO
Veterinary Ophthalmologist

Phone: 250.418.3097
Email: tessalyanimaleyecare@mailbrook.net
Website: tessalyanimaleyecare.net
Address: 1840 Pellworth Rd
Kelowna, BC, V4T 8M3

Colors

Designer to choose colors to be used in the design.

Requirements
Must have
• Our logo (attached)

```html
<!DOCTYPE html>
<html lang="en">
<head>
<meta charset="utf-8">
<title>Tessaly Animal Eye Care – Business Card Back</title>
<link rel="stylesheet" href="https://fonts.googleapis.com/css2?family=Gelasio:wght@400;700&family=Open+Sans:wght@400&display=swap">
<style>
  :root {
    --teal: #30c5ad;
    --slate: #667b7b;
    --ink: #000000;
    --paper: #ffffff;
  }
  html, body {
    margin: 0;
    padding: 0;
    width: 1200px;
    height: 809px;
    overflow: hidden;
    background: var(--paper);
  }
  .card-sheet {
    display: block;
    width: 1200px;
    height: 809px;
  }
  .side-label {
    font-family: "Open Sans", Arial, sans-serif;
    font-size: 46px;
    letter-spacing: 4px;
    fill: var(--ink);
  }
  .contact {
    font-family: "Gelasio", "Palatino Linotype", Palatino, serif;
    fill: var(--teal);
    text-anchor: middle;
  }
  .contact-name {
    font-weight: 700;
    font-size: 32px;
  }
  .contact-line {
    font-weight: 400;
    font-size: 29.5px;
  }
  .crop-mark { stroke: var(--ink); stroke-width: 1; }
  .crop-mark--on-band { stroke: var(--paper); stroke-width: 1; }
  .band--teal { fill: var(--teal); }
  .band--slate { fill: var(--slate); }
</style>
</head>
<body>
<svg class="card-sheet" viewBox="0 0 1200 809" xmlns="http://www.w3.org/2000/svg">
  <!-- Header bands -->
  <g class="header-bands">
    <rect class="band--teal" x="212" y="190" width="775" height="37"/>
    <rect class="band--slate" x="212" y="227" width="775" height="11"/>
    <rect class="band--teal" x="212" y="238" width="775" height="12"/>
    <rect class="band--slate" x="212" y="250" width="775" height="11"/>
  </g>

  <!-- Trim marks -->
  <g class="trim-marks">
    <line class="crop-mark" x1="238" y1="122" x2="238" y2="190"/>
    <line class="crop-mark--on-band" x1="238" y1="190" x2="238" y2="198"/>
    <line class="crop-mark" x1="961" y1="122" x2="961" y2="190"/>
    <line class="crop-mark--on-band" x1="961" y1="190" x2="961" y2="198"/>
    <line class="crop-mark" x1="143" y1="216" x2="212" y2="216"/>
    <line class="crop-mark--on-band" x1="212" y1="216" x2="220" y2="216"/>
    <line class="crop-mark--on-band" x1="978" y1="216" x2="987" y2="216"/>
    <line class="crop-mark" x1="987" y1="216" x2="1055" y2="216"/>

    <line class="crop-mark" x1="143" y1="626" x2="220" y2="626"/>
    <line class="crop-mark" x1="978" y1="626" x2="1055" y2="626"/>
    <line class="crop-mark" x1="238" y1="643" x2="238" y2="720"/>
    <line class="crop-mark" x1="961" y1="643" x2="961" y2="720"/>
  </g>

  <text class="side-label" x="30" y="476">Back</text>

  <!-- Contact block -->
  <g class="contact">
    <text class="contact-name" x="599" y="330">Marisol Dunkley, BSc, DVM, MSc, DipACVO</text>
    <text class="contact-line" x="599" y="370">Veterinary Ophthalmologist</text>
    <text class="contact-line" x="599" y="410">Phone: 250.418.3097</text>
    <text class="contact-line" x="599" y="450">Email: tessalyanimaleyecare@mailbrook.net</text>
    <text class="contact-line" x="599" y="490">Website: tessalyanimaleyecare.net</text>
    <text class="contact-line" x="599" y="530">Address: 1840 Pellworth Rd</text>
    <text class="contact-line" x="599" y="570">Kelowna, BC, V4T 8M3</text>
  </g>
</svg>
</body>
</html>
```